Instructions for nurses on how to give a report on each shift

I have a 2-page reference sheet that needs to be updated to look more aesthetically pleasing.

Target Market(s)

Healthcare, nurses

Industry/Entity Type

Healthcare

Font styles to use
Sans Serif

Requirements
Must have
• Please make sure it is easy to read, the content is well organized and has a flow to it. Please also pick colors that would coordinate with our website www.ovtrime.org (so mainly navy and white or off-white with accent colors.) Please make sure to add accent colors to break up the content. The BORSK name and title at the top should remain on the page but I'm not married to the star or logo style. You can do what you think looks best there. Way at the bottom in fine print, I would like for you to add OVTRIME © 2019 All rights reserved.

```html
<!DOCTYPE html>
<html lang="en">
<head>
<meta charset="utf-8">
<title>BORSKR – Shift Report Reference</title>
<link href="https://fonts.googleapis.com/css2?family=Open+Sans:wght@400;600;700&display=swap" rel="stylesheet">
<style>
  :root{
    --navy:#0c3a60;
    --navy-deep:#0a3257;
    --sky:#c9e6f8;
    --sky-strip:#d9eefb;
    --white:#ffffff;
    --ink:#0c3a60;
  }
  *{box-sizing:border-box;margin:0;padding:0}
  html,body{width:902px;height:1200px;overflow:hidden}
  body{background:var(--navy);font-family:"Open Sans",Arial,sans-serif;color:var(--ink);position:relative}
  .sheet{position:absolute;left:97px;background:var(--sky);overflow:hidden}
  .sheet--flow{top:81px;width:708px;height:500px}
  .sheet--guide{top:617px;width:712px;height:502px}
  .sheet__strip{height:14px;background:var(--sky-strip)}
  .sheet__band{height:50px;background:var(--navy);display:flex;align-items:center;justify-content:space-between;padding:0 32px 0 38px}
  .sheet__title{color:var(--white);font-size:25px;font-weight:700;letter-spacing:.5px}
  .sheet__tagline{color:var(--white);font-size:10.5px;line-height:13px;text-align:right;letter-spacing:.2px}
  .flowchart{display:block}
  .flowchart text{font-family:"Open Sans",Arial,sans-serif;fill:var(--ink)}
  .flowchart .t-label{font-size:11.5px;font-weight:600}
  .flowchart .t-label-sm{font-size:10.5px;font-weight:600}
  .flowchart .t-bullet{font-size:10.5px}
  .flowchart .t-box-head{font-size:11px;font-weight:700;fill:var(--white)}
  .flowchart .t-box{font-size:9.3px;fill:var(--white)}
  .flowchart .t-tab{font-size:13px;font-weight:700;fill:var(--white)}
  .flowchart .t-field{font-size:10.5px;font-weight:600}
  .flowchart .t-foot{font-size:11px}
  .line{stroke:var(--navy);stroke-width:1.6;fill:none}
  .quote{position:absolute;top:91px;left:0;width:100%;text-align:center;font-size:18.5px;font-weight:700;color:var(--ink)}
  .topic{position:absolute}
  .topic__icon{display:block;width:24px;height:22px}
  .topic__head{font-size:10px;font-weight:600;letter-spacing:.2px;margin-top:3px}
  .topic__list{list-style:none;margin-top:8px;font-size:8.4px;line-height:9.8px}
  .topic__list li{position:relative;padding-left:30px}
  .topic__list li::before{content:"";position:absolute;left:14px;top:3.6px;width:3px;height:3px;border-radius:50%;background:var(--ink)}
  .topic--objectives{left:54px;top:137px;width:290px}
  .topic--outcomes{left:54px;top:244px;width:290px}
  .topic--who{left:54px;top:349px;width:290px}
  .topic--when{left:358px;top:141px;width:290px}
  .topic--where{left:358px;top:217px;width:290px}
  .topic--tips{left:358px;top:278px;width:272px}
  .topic--tips .topic__list{margin-top:6px;letter-spacing:-.1px}
  .sheet__foot{position:absolute;left:43px;right:43px;top:467px;display:flex;align-items:center;gap:10px;font-size:8.8px}
  .sheet__foot::before,.sheet__foot::after{content:"";flex:1;height:1px;background:var(--navy)}
</style>
</head>
<body>

<section class="sheet sheet--flow">
  <div class="sheet__strip"></div>
  <header class="sheet__band">
    <h1 class="sheet__title">BORSKR</h1>
    <p class="sheet__tagline">BRIEFING EVERY SHIFT WITH CARE,<br>CLARITY AND SHARED PURPOSE</p>
  </header>
  <svg class="flowchart" width="708" height="436" viewBox="0 80 885 545">
    <circle cx="442" cy="104" r="15" fill="none" stroke="#0c3a60" stroke-width="2"/>
    <circle cx="442" cy="100" r="5.5" fill="#0c3a60"/>
    <path d="M432 114 q10 -10 20 0 z" fill="#0c3a60"/>
    <rect x="350" y="123" width="184" height="61" fill="none" stroke="#0c3a60" stroke-width="1.6"/>
    <rect x="350" y="123" width="184" height="16" rx="6" fill="#0c3a60"/>
    <text class="t-tab" x="442" y="136" text-anchor="middle">BORSKR</text>
    <text class="t-field" x="361" y="154">Name:</text>
    <text class="t-field" x="361" y="166">Title:</text>
    <text class="t-field" x="361" y="178">Assignment:</text>

    <path class="line" d="M442 184 V210 M114 210 H769 M114 210 V240 M280 210 V240 M442 210 V240 M605 210 V240 M769 210 V240"/>

    <path class="line" d="M128 257 H202 V376 H113 V414 M71 432 V414 H151 V432"/>
    <path class="line" d="M294 257 H366 V376 H277 V414 M234 432 V414 H314 V432"/>
    <path class="line" d="M456 257 H527 V376 H439 V414 M396 432 V414 H476 V432"/>
    <path class="line" d="M619 257 H687 V376 H598 V414 M558 432 V414 H638 V432"/>
    <path class="line" d="M783 257 H849 V376 H760 V414 M720 432 V414 H800 V432"/>

    <g fill="#0c3a60">
      <path d="M103 240 h16 l6 6 v22 h-22 z"/>
      <path d="M109 249 h6 M112 246 v6" stroke="#c9e6f8" stroke-width="1.6"/>
      <path d="M113 258 h7 M113 262 h7" stroke="#c9e6f8" stroke-width="1.3"/>
    </g>
    <g fill="none" stroke="#0c3a60" stroke-width="1.6">
      <rect x="267" y="246" width="22" height="15" rx="1"/>
      <path d="M267 261 h-2 v-8 l5 -5"/>
      <circle cx="282" cy="253" r="4"/>
      <path d="M282 250.5 v5 M279.5 253 h5"/>
      <circle cx="271" cy="264" r="2.5" fill="#c9e6f8"/>
      <circle cx="284" cy="264" r="2.5" fill="#c9e6f8"/>
    </g>
    <g fill="none" stroke="#0c3a60" stroke-width="1.6">
      <rect x="429" y="242" width="27" height="18" rx="1"/>
      <path d="M438 264 h9 M442 260 v4"/>
      <circle cx="442" cy="251" r="5"/>
      <path d="M442 248 v6 M439 251 h6"/>
    </g>
    <g fill="none" stroke="#0c3a60" stroke-width="1.6">
      <path d="M598 244 v14"/>
      <circle cx="598" cy="262" r="3.5" fill="#0c3a60"/>
      <circle cx="611" cy="253" r="3" fill="#0c3a60"/>
      <path d="M611 246 v2 M611 258 v2 M604 253 h2 M616 253 h2 M606 248 l1.5 1.5 M614.5 256.5 l1.5 1.5 M606 258 l1.5 -1.5 M614.5 249.5 l1.5 -1.5"/>
    </g>
    <g fill="#0c3a60">
      <rect x="764" y="240" width="11" height="11" rx="1.5"/>
      <path d="M769.5 242.5 v6 M766.5 245.5 h6" stroke="#c9e6f8" stroke-width="1.6"/>
      <path d="M755 258 q6 -4 12 -1 h10 q3 0 3 2.5 h-9 h10 l8 -5 q3 0 2 3 l-9 8 h-27 z"/>
    </g>

    <text class="t-label" x="62" y="285"><tspan x="62">Any change in resident</tspan><tspan x="62" dy="14">status?</tspan></text>
    <text class="t-bullet"><tspan x="66" y="325">• Admissions</tspan><tspan x="66" dy="14">• Discharges</tspan><tspan x="66" dy="14">• Transfers</tspan><tspan x="66" dy="14">• Appointments</tspan></text>

    <text class="t-label" x="216" y="285"><tspan x="216">Any concerning changes</tspan><tspan x="216" dy="14">in resident's condition?</tspan></text>
    <text class="t-bullet"><tspan x="217" y="324">• Pain</tspan><tspan x="217" dy="12.5">• Ambulation</tspan><tspan x="217" dy="12.5">• Behavior</tspan><tspan x="217" dy="12.5">• Elimination</tspan></text>
    <text class="t-bullet"><tspan x="293" y="324">• Skin</tspan><tspan x="293" dy="12.5">• Safety</tspan><tspan x="293" dy="12.5">• Appetite</tspan></text>

    <text class="t-label" x="381" y="285"><tspan x="381">Any residents requiring</tspan><tspan x="381" dy="14">extraordinary monitoring?</tspan></text>
    <text class="t-bullet"><tspan x="385" y="323">• Falls</tspan><tspan x="385" dy="12.5">• Decline in condition</tspan><tspan x="385" dy="12.5">• IV/ABT therapy</tspan><tspan x="385" dy="12.5">• Hospice</tspan></text>

    <text class="t-label" x="554" y="285"><tspan x="554">Any concerns related</tspan><tspan x="554" dy="14">to residents</tspan><tspan x="554" dy="14">environment?</tspan></text>
    <text class="t-bullet"><tspan x="558" y="338">• Room temperature</tspan><tspan x="558" dy="12.5">• Supplies</tspan><tspan x="558" dy="12.5">• Equipment</tspan></text>

    <text class="t-label-sm" x="697" y="283"><tspan x="697">Any concerns or barriers</tspan><tspan x="697" dy="12.5">related to your ability to</tspan><tspan x="697" dy="12.5">perform your job effectively?</tspan></text>
    <text class="t-bullet"><tspan x="700" y="334">• Supplies</tspan><tspan x="700" dy="12.5">• Time constraints</tspan><tspan x="700" dy="12.5">• Family requests</tspan><tspan x="700" dy="12.5">• Environment</tspan></text>
    <text class="t-bullet" x="753" y="334">• Acuity</text>

    <g fill="#0a3257">
      <rect x="40" y="432" width="65" height="135" rx="8"/><rect x="118" y="432" width="66" height="135" rx="8"/>
      <rect x="202" y="432" width="65" height="135" rx="8"/><rect x="280" y="432" width="66" height="135" rx="8"/>
      <rect x="364" y="432" width="65" height="135" rx="8"/><rect x="442" y="432" width="66" height="135" rx="8"/>
      <rect x="526" y="432" width="65" height="135" rx="8"/><rect x="604" y="432" width="66" height="135" rx="8"/>
      <rect x="688" y="432" width="65" height="135" rx="8"/><rect x="766" y="432" width="66" height="135" rx="8"/>
    </g>
    <g text-anchor="middle">
      <text class="t-box-head" x="72" y="452">NO</text><text class="t-box-head" x="151" y="450">YES</text>
      <text class="t-box-head" x="234" y="452">NO</text><text class="t-box-head" x="313" y="450">YES</text>
      <text class="t-box-head" x="396" y="452">NO</text><text class="t-box-head" x="475" y="450">YES</text>
      <text class="t-box-head" x="558" y="450">NO</text><text class="t-box-head" x="637" y="450">YES</text>
      <text class="t-box-head" x="720" y="452">NO</text><text class="t-box-head" x="799" y="450">YES</text>

      <text class="t-box"><tspan x="72" y="477">“I do not</tspan><tspan x="72" dy="11.5">have any</tspan><tspan x="72" dy="11.5">actual or</tspan><tspan x="72" dy="11.5">expected</tspan><tspan x="72" dy="11.5">changes in</tspan><tspan x="72" dy="11.5">resident</tspan><tspan x="72" dy="11.5">status.”</tspan></text>
      <text class="t-box"><tspan x="151" y="472">“My residents</tspan><tspan x="151" dy="11.5">with changes</tspan><tspan x="151" dy="11.5">in their status</tspan><tspan x="151" dy="11.5">are…”</tspan></text>

      <text class="t-box"><tspan x="234" y="477">“I have no</tspan><tspan x="234" dy="11.5">residents</tspan><tspan x="234" dy="11.5">with</tspan><tspan x="234" dy="11.5">concerning</tspan><tspan x="234" dy="11.5">changes in</tspan><tspan x="234" dy="11.5">their</tspan><tspan x="234" dy="11.5">condition.”</tspan></text>
      <text class="t-box"><tspan x="313" y="472">“My residents</tspan><tspan x="313" dy="11.5">w/ concerning</tspan><tspan x="313" dy="11.5">changes in</tspan><tspan x="313" dy="11.5">their condition</tspan><tspan x="313" dy="11.5">include…”</tspan></text>

      <text class="t-box"><tspan x="396" y="477">“I have no</tspan><tspan x="396" dy="11.5">residents</tspan><tspan x="396" dy="11.5">requiring</tspan><tspan x="396" dy="11.5">extraordi-</tspan><tspan x="396" dy="11.5">nary</tspan><tspan x="396" dy="11.5">monitor-</tspan><tspan x="396" dy="11.5">ing.”</tspan></text>
      <text class="t-box"><tspan x="475" y="472">“My residents</tspan><tspan x="475" dy="11.5">that require</tspan><tspan x="475" dy="11.5">extraordinary</tspan><tspan x="475" dy="11.5">monitoring</tspan><tspan x="475" dy="11.5">are…”</tspan></text>

      <text class="t-box"><tspan x="558" y="472">“I have no</tspan><tspan x="558" dy="11.5">concerns</tspan><tspan x="558" dy="11.5">related to my</tspan><tspan x="558" dy="11.5">residents</tspan><tspan x="558" dy="11.5">environment.”</tspan></text>
      <text class="t-box"><tspan x="637" y="472">“My residents</tspan><tspan x="637" dy="11.5">with concerns</tspan><tspan x="637" dy="11.5">related to their</tspan><tspan x="637" dy="11.5">environment</tspan><tspan x="637" dy="11.5">include…”</tspan></text>

      <text class="t-box"><tspan x="720" y="477">“I have no</tspan><tspan x="720" dy="11.5">concerns</tspan><tspan x="720" dy="11.5">or barriers</tspan><tspan x="720" dy="11.5">affecting</tspan><tspan x="720" dy="11.5">my ability</tspan><tspan x="720" dy="11.5">to perform</tspan><tspan x="720" dy="11.5">my job.”</tspan></text>
      <text class="t-box"><tspan x="799" y="472">“My concerns</tspan><tspan x="799" dy="11.5">affecting my</tspan><tspan x="799" dy="11.5">ability to</tspan><tspan x="799" dy="11.5">perform my</tspan><tspan x="799" dy="11.5">job include…”</tspan></text>
    </g>
    <g>
      <text class="t-box"><tspan x="124" y="531">1)__________</tspan><tspan x="124" dy="11">2)__________</tspan><tspan x="124" dy="11">3)__________</tspan></text>
      <text class="t-box"><tspan x="286" y="531">1)__________</tspan><tspan x="286" dy="11">2)__________</tspan><tspan x="286" dy="11">3)__________</tspan></text>
      <text class="t-box"><tspan x="448" y="531">1)__________</tspan><tspan x="448" dy="11">2)__________</tspan><tspan x="448" dy="11">3)__________</tspan></text>
      <text class="t-box"><tspan x="610" y="531">1)__________</tspan><tspan x="610" dy="11">2)__________</tspan><tspan x="610" dy="11">3)__________</tspan></text>
      <text class="t-box"><tspan x="772" y="531">1)__________</tspan><tspan x="772" dy="11">2)__________</tspan><tspan x="772" dy="11">3)__________</tspan></text>
    </g>

    <path class="line" stroke-width="1" d="M53 591 H343 M541 591 H830"/>
    <text class="t-foot" x="442" y="593" text-anchor="middle">OVTRIME © 2019 All rights reserved.</text>
  </svg>
</section>

<section class="sheet sheet--guide">
  <div class="sheet__strip"></div>
  <header class="sheet__band">
    <h1 class="sheet__title">BORSKR</h1>
    <p class="sheet__tagline">BRIEFING EVERY SHIFT WITH CARE,<br>CLARITY AND SHARED PURPOSE</p>
  </header>

  <h2 class="quote">When “I” is replaced by “WE” Even illness becomes wellness.</h2>

  <div class="topic topic--objectives">
    <svg class="topic__icon" viewBox="0 0 24 22"><path d="M2 7 V2 H7 M17 2 H22 V7 M22 15 V20 H17 M7 20 H2 V15 M12 8 V14 M9 11 H15" fill="none" stroke="#0c3a60" stroke-width="2"/></svg>
    <h3 class="topic__head">OBJECTIVES:</h3>
    <ul class="topic__list">
      <li>Accountability: Declare roles and assignments</li>
      <li>Advocacy: Identify patient needs</li>
      <li>Critical Thinking: Prioritize and recognize obstacles</li>
      <li>Communication: Share important information</li>
      <li>Collaboration: Utilize an interdisciplinary approach</li>
    </ul>
  </div>

  <div class="topic topic--outcomes">
    <svg class="topic__icon" viewBox="0 0 24 22"><path d="M10 1 h4 v4 h4 v4 h-4 v4 h-4 v-4 h-4 v-4 h4 z" fill="#0c3a60"/><path d="M2 8 q-1 6 3 10 h3 v-5 l-3 -4 M22 8 q1 6 -3 10 h-3 v-5 l3 -4" fill="none" stroke="#0c3a60" stroke-width="2"/></svg>
    <h3 class="topic__head">OUTCOMES:</h3>
    <ul class="topic__list">
      <li>Share best practices</li>
      <li>Improve communication</li>
      <li>Promote cohesiveness</li>
      <li>Increase staff morale</li>
      <li>Enhance patient and organizational outcomes</li>
    </ul>
  </div>

  <div class="topic topic--who">
    <svg class="topic__icon" viewBox="0 0 34 22" style="width:34px"><g fill="#0c3a60"><circle cx="7" cy="8" r="3.5"/><circle cx="17" cy="6" r="4"/><circle cx="27" cy="8" r="3.5"/><path d="M1 21 q0 -8 6 -8 q6 0 6 8 z M10 21 q0 -10 7 -10 q7 0 7 10 z M21 21 q0 -8 6 -8 q6 0 6 8 z"/></g></svg>
    <h3 class="topic__head">WHO:</h3>
    <ul class="topic__list">
      <li>All nurses on the unit</li>
      <li>All nursing support staff (CNA/MA/HCT)</li>
      <li>Administrator</li>
      <li>Director of Nursing</li>
      <li>Head of pertinent disciplines (Dietary, Social Work, Physical Therapy, Engineering, Central Supply, etc.)</li>
    </ul>
  </div>

  <div class="topic topic--when">
    <svg class="topic__icon" viewBox="0 0 34 22" style="width:34px"><g fill="#0c3a60"><circle cx="6" cy="4" r="3"/><circle cx="17" cy="3.5" r="3"/><circle cx="28" cy="4" r="3"/><rect x="1" y="9" width="32" height="3"/><rect x="11" y="12" width="12" height="9"/><path d="M1 21 v-8 h4 v8 z M29 21 v-8 h4 v8 z"/></g><path d="M17 14 v5 M14.5 16.5 h5" stroke="#c9e6f8" stroke-width="1.6"/></svg>
    <h3 class="topic__head">WHEN:</h3>
    <ul class="topic__list">
      <li>Every morning (assign a meeting time for each unit )</li>
      <li>Keep meetings within 15 minutes in length</li>
    </ul>
  </div>

  <div class="topic topic--where">
    <svg class="topic__icon" viewBox="0 0 24 22"><path d="M12 1 L23 10 H20 V21 H4 V10 H1 Z" fill="#0c3a60"/><circle cx="12" cy="14" r="4.2" fill="#c9e6f8"/><path d="M12 11.5 v5 M9.5 14 h5" stroke="#0c3a60" stroke-width="1.6"/></svg>
    <h3 class="topic__head">WHERE:</h3>
    <ul class="topic__list">
      <li>Nursing station on each unit</li>
    </ul>
  </div>

  <div class="topic topic--tips">
    <svg class="topic__icon" viewBox="0 0 24 22"><circle cx="12" cy="9" r="6" fill="#0c3a60"/><rect x="9" y="14" width="6" height="5" fill="#0c3a60"/><path d="M12 6.5 v5 M9.5 9 h5" stroke="#c9e6f8" stroke-width="1.6"/><path d="M1 9 h2 M21 9 h2 M4 2 l1.5 1.5 M20 2 l-1.5 1.5 M12 0 v1" stroke="#0c3a60" stroke-width="1.4"/></svg>
    <h3 class="topic__head">HELPFUL TIPS:</h3>
    <ul class="topic__list">
      <li>Assign a meeting facilitator (usually the administrator of the facility)</li>
      <li>Standing during meetings keeps the meetings short and to the point</li>
      <li>Keeping meetings within 15 minutes emphasizes being prepared and direct</li>
      <li>Keep meeting times consistent (morning is best)</li>
      <li>Do not begin until everyone is present (minimizes stragglers)</li>
      <li>Avoid discussing personal concerns</li>
      <li>Include reminders for in-services, meetings, etc. and updates towards the end of the meeting</li>
      <li>Always conclude with achievements, milestones, praise, words of encouragement, motivational quote, etc.</li>
    </ul>
  </div>

  <footer class="sheet__foot">OVTRIME © 2019 All rights reserved.</footer>
</section>

</body>
</html>
```